Halvorine Ledgers & Advisory Tri-Fold Brochure (8.5"x11")

I need a professional looking brochure for my bookkeeping business. I am looking for something professional yet casual (not too corporate looking). I have attached a sample brochure that will outline the areas and a copy of our logo. I'd like to stick with shades of blue. The final product should communicate professional and personal.

Target Market(s)

Small service businesses.

Industry/Entity Type

Business

Font styles to use
Sans Serif

Requirements
Must have
• Professional looking photos of people in areas where it asks for a picture.

```html
<!DOCTYPE html>
<html lang="en">
<head>
<meta charset="utf-8">
<title>Halvorine Ledgers &amp; Advisory – Tri-Fold Brochure</title>
<link rel="stylesheet" href="https://fonts.googleapis.com/css2?family=Open+Sans:wght@400;600;700&display=swap">
<style>
  :root {
    --blue-strong: #1a6fc4;
    --blue-band: #3f8fd6;
    --blue-soft: #95bde6;
    --blue-pale: #cfe3f6;
    --bg-top: #f3f8fd;
    --bg-bottom: #d3e6f7;
    --ink: #4a4a4a;
    --ink-dark: #2e3338;
    --white: #ffffff;
    --font: "Open Sans", Arial, sans-serif;
  }
  html, body { margin: 0; padding: 0; overflow: hidden; }
  body { width: 1200px; height: 927px; font-family: var(--font); }
  .brochure {
    position: relative; width: 1200px; height: 927px; overflow: hidden;
    background: linear-gradient(180deg, var(--bg-top) 0%, var(--bg-bottom) 100%);
  }
  .abs { position: absolute; }
  .photo { position: absolute; }

  /* Left panel */
  .photo-globe { left: 18px; top: 0; width: 184px; height: 202px;
    background: linear-gradient(160deg, #1d4f86 0%, #5f8fc4 55%, #c6d8ec 100%); }
  .photo-ledger { left: 121px; top: 152px; width: 240px; height: 159px;
    background: linear-gradient(135deg, #e7eef6 0%, #b9cde3 60%, #8ea9c9 100%);
    box-shadow: 0 0 0 3px var(--white); }
  .intro-heading { left: 0; top: 338px; width: 397px; margin: 0; text-align: center;
    color: var(--blue-strong); font-size: 25px; font-weight: 600; line-height: 1.22; }
  .intro-label { left: 27px; top: 428px; margin: 0; color: var(--ink); font-size: 19px; }
  .intro-copy { left: 27px; top: 474px; width: 346px; margin: 0; color: var(--ink);
    font-size: 15.4px; line-height: 17.6px; text-align: justify; }
  .cta-box { left: 0; top: 727px; width: 382px; height: 174px; background: var(--blue-pale); }
  .cta-rule { position: absolute; left: 95px; top: 30px; width: 227px; height: 1px; background: var(--ink-dark); }
  .cta-text { position: absolute; left: 0; top: 48px; width: 382px; margin: 0; text-align: center;
    color: var(--blue-strong); font-size: 25px; font-weight: 700; line-height: 1.3; }

  /* Middle panel */
  .photo-handshake { left: 409px; top: 0; width: 378px; height: 579px;
    background: linear-gradient(180deg, #3d6f9c 0%, #b9d3ea 45%, #5f7f9c 70%, #24384e 100%); }
  .contact-title { left: 409px; top: 590px; width: 378px; margin: 0; text-align: center;
    color: var(--blue-strong); font-size: 36px; font-weight: 600; }
  .contact-rule { left: 492px; top: 647px; width: 231px; height: 1px; background: var(--ink-dark); }
  .contact-list { left: 421px; top: 658px; margin: 0; padding: 0; list-style: none; }
  .contact-list li { display: flex; align-items: center; height: 30px; margin-bottom: 20px;
    color: var(--blue-strong); font-size: 20px; }
  .contact-list svg { width: 26px; height: 26px; margin-right: 14px; flex: none; }
  .tagline-band { height: 61px; background: var(--blue-band); color: var(--white);
    display: flex; align-items: center; justify-content: center; font-size: 19px; font-weight: 600; }
  .band-middle { left: 412px; top: 842px; width: 376px; }

  /* Right panel */
  .photo-meeting { left: 818px; top: 0; width: 382px; height: 427px;
    background: linear-gradient(180deg, #e9f1f8 0%, #c4d6e6 45%, #53637a 80%, #2c3546 100%); }
  .band-right { left: 818px; top: 427px; width: 382px; }
  .brand { left: 818px; top: 508px; width: 382px; text-align: center; color: var(--blue-strong); }
  .brand-mark { display: block; margin: 0 auto 12px; width: 38px; height: 38px; border-radius: 50%; background: var(--blue-strong); }
  .brand-name { margin: 0; font-size: 22px; font-weight: 600; line-height: 1.2; }
  .brand-place { margin: 6px 0 0; font-size: 14px; color: var(--ink-dark); }
  .brand-rule { left: 882px; top: 692px; width: 227px; height: 1px; background: var(--ink-dark); }
  .promise-box { left: 818px; top: 712px; width: 382px; height: 191px; background: var(--blue-soft);
    display: flex; align-items: center; justify-content: center; }
  .promise-text { margin: 0; width: 300px; text-align: center; color: var(--white);
    font-size: 28px; font-weight: 700; line-height: 1.3; }
</style>
</head>
<body>
<main class="brochure">

  <!-- Left panel: services -->
  <section class="panel-services">
    <div class="photo photo-globe" role="img" aria-label="Photo of a glass globe resting on financial papers"></div>
    <div class="photo photo-ledger" role="img" aria-label="Photo of spreadsheets with glasses, a pen and a calculator"></div>
    <h2 class="abs intro-heading">HERE TO SIMPLITY THE<br>BOOKKEEPING PROCESS</h2>
    <p class="abs intro-label">What we do:</p>
    <p class="abs intro-copy">Allow business owners to spend more time focusing on their core business by providing comprehensive bookkeeping and business consulting services. We provide the financial data and tools that allow businesses to maximize profitability and focus on growth and other areas of their business. We consider our business to be an extension of your business and look forward to the opportunity to exceed your expectations!</p>
    <div class="abs cta-box">
      <span class="cta-rule"></span>
      <p class="cta-text">Let’s talk<br>Schedule a no-obligation<br>consultation today</p>
    </div>
  </section>

  <!-- Middle panel: contact -->
  <section class="panel-contact">
    <div class="photo photo-handshake" role="img" aria-label="Photo of silhouetted business people shaking hands by a bright office window"></div>
    <h2 class="abs contact-title">Contact Us</h2>
    <span class="abs contact-rule"></span>
    <ul class="abs contact-list">
      <li>
        <svg viewBox="0 0 26 26" aria-hidden="true"><circle cx="13" cy="13" r="13" fill="#2e3338"/><path d="M9 7.5c.6-.5 1.4-.4 1.8.2l1.2 1.9c.3.5.2 1.1-.2 1.5l-.8.7c.7 1.5 1.8 2.6 3.3 3.3l.7-.8c.4-.4 1-.5 1.5-.2l1.9 1.2c.6.4.7 1.2.2 1.8l-.9 1c-.6.6-1.5.8-2.3.5-3.3-1.2-5.8-3.7-7-7-.3-.8-.1-1.7.5-2.3z" fill="#fff"/></svg>
        Phone: 555.014.0372
      </li>
      <li>
        <svg viewBox="0 0 26 26" aria-hidden="true"><circle cx="13" cy="13" r="13" fill="#2e3338"/><rect x="7" y="8.5" width="12" height="9" rx="1" fill="none" stroke="#fff" stroke-width="1.6"/><path d="M7.5 9.3 13 13.6l5.5-4.3" fill="none" stroke="#fff" stroke-width="1.6"/></svg>
        Email: mara@halvorineledgers.com
      </li>
      <li>
        <svg viewBox="0 0 26 26" aria-hidden="true"><circle cx="13" cy="13" r="13" fill="#2e3338"/><g fill="none" stroke="#fff" stroke-width="1.4"><circle cx="13" cy="13" r="6.5"/><ellipse cx="13" cy="13" rx="2.8" ry="6.5"/><path d="M6.5 13h13M7.5 9.8h11M7.5 16.2h11"/></g></svg>
        Web: www.halvorineledgers.com
      </li>
    </ul>
    <div class="abs tagline-band band-middle">Trustworthy - Experienced - Reliable</div>
  </section>

  <!-- Right panel: cover -->
  <section class="panel-cover">
    <div class="photo photo-meeting" role="img" aria-label="Photo of two business professionals reviewing a document in a bright office"></div>
    <div class="abs tagline-band band-right">Trustworthy - Experienced - Reliable</div>
    <div class="abs brand">
      <span class="brand-mark"></span>
      <p class="brand-name">Halvorine Ledgers &amp; Advisory</p>
      <p class="brand-place">Marrowby Valley, PA</p>
    </div>
    <span class="abs brand-rule"></span>
    <div class="abs promise-box">
      <p class="promise-text">Expert bookkeeping services for small businesses</p>
    </div>
  </section>

</main>
</body>
</html>
```